Coffee House With Cycling Theme Wants Business Cards

We want to create a business card for a coffee house that has a cycling theme. We expect to use the current logo on one side of the business card and we have been considering adding the words 'COFFEE HOUSE' underneath (see example). For the other side of the business card we want an interesting design with tag-line, address and social media links (the normal business card stuff). See examples provided but we are not fixed on having it exactly as shown, we are very open to great creative ideas. Please note our logo has the initials ‘RM' in orange embedded in the design and this must be retained. However, you can play with the words COFFEE HOUSE as well as use the orange color on the backside of the business card, as you see fit. For an image on the backside of the business card it can be a photo, hand-drawn or whatever but it must visually combine coffee and cycling in some way. The interior of the Coffee House will be reclaimed wood, rustic and have an urban feel to it with cycling artifacts hanging from the walls/ceiling, etc. Finally, it would be beneficial if the business card design elements can be easily used on flyers and other promotional assets. Good luck, we are looking forward to seeing your creative ideas.

Target Market(s)

Coffee lovers and cycling fans

Contact Information for Business Card

See project description.

Colors

Designer to choose colors to be used in the design.

Requirements
Must have
• Must use the current logo provided and combine a coffee and bike theme.
Nice to have
• Orange is used in current logo and could be used as an accent color on the backside of the business card.

```html
<!DOCTYPE html>
<html lang="en">
<head>
<meta charset="utf-8">
<title>RM Coffee House – Business Card</title>
<link rel="stylesheet" href="https://fonts.googleapis.com/css2?family=Oswald:wght@500&family=Work+Sans:wght@400;500&display=swap">
<style>
  :root {
    --bg: #1f1f1f;
    --orange: #f06a2e;
    --orange-light: #f37c45;
    --white: #ffffff;
    --ink: #2b2b2b;
    --grey-band: #3a3a3a;
  }
  * { box-sizing: border-box; margin: 0; padding: 0; }
  html, body { width: 1200px; height: 900px; overflow: hidden; }
  body {
    background: radial-gradient(circle at 70% 20%, #2e2e2e, var(--bg) 70%);
    font-family: "Work Sans", sans-serif;
    position: relative;
  }
  .card {
    position: absolute;
    left: 270px;
    width: 660px;
    height: 377px;
    box-shadow: 0 10px 30px rgba(0,0,0,.5);
  }
  .card-front {
    top: 48px;
    background: linear-gradient(120deg, var(--orange), var(--orange-light));
    display: flex;
    align-items: center;
    justify-content: center;
  }
  .brand-name {
    color: var(--white);
    font-weight: 500;
    font-size: 44px;
    letter-spacing: 3px;
    text-align: center;
    line-height: 1.2;
  }
  .card-back {
    top: 473px;
    background: var(--white);
    color: var(--ink);
  }
  .identity {
    position: absolute;
    top: 132px;
    right: 370px;
    text-align: right;
  }
  .person-name {
    font-family: "Oswald", sans-serif;
    font-weight: 500;
    font-size: 40px;
    color: var(--orange);
    letter-spacing: 1px;
    line-height: 1;
  }
  .person-title { font-size: 17px; margin-top: 6px; }
  .divider {
    position: absolute;
    left: 310px;
    top: 132px;
    width: 2px;
    height: 72px;
    background: var(--orange);
  }
  .contacts {
    position: absolute;
    left: 332px;
    top: 130px;
    list-style: none;
    font-size: 17px;
    line-height: 26px;
  }
  .contacts li { display: flex; align-items: center; gap: 10px; }
  .contacts svg { width: 12px; height: 12px; flex: none; }
  .address {
    position: absolute;
    left: 0; right: 0;
    top: 262px;
    text-align: center;
    font-size: 17px;
  }
  .socials {
    position: absolute;
    left: 0; right: 0;
    top: 294px;
    display: flex;
    justify-content: center;
    gap: 28px;
    font-size: 16px;
  }
  .socials span { display: flex; align-items: center; gap: 8px; }
  .social-square { width: 16px; height: 16px; background: #2f6fb7; }
  .social-circle { width: 16px; height: 16px; border-radius: 50%; background: #d6417b; }
  .band {
    position: absolute;
    bottom: 0;
    height: 10px;
  }
  .band-grey { left: 0; width: 50%; background: var(--grey-band); }
  .band-orange { right: 0; width: 50%; background: var(--orange); }
</style>
</head>
<body>
  <section class="card card-front">
    <p class="brand-name">RM<br>COFFEE HOUSE</p>
  </section>

  <section class="card card-back">
    <div class="identity">
      <h1 class="person-name">DANIEL REYES</h1>
      <p class="person-title">Director</p>
    </div>
    <div class="divider"></div>
    <ul class="contacts">
      <li>
        <svg viewBox="0 0 12 12"><path d="M3 1 L5 3 L4 4.5 Q5 7 7.5 8 L9 7 L11 9 L9.5 11 Q3 10 1 2.5 Z" fill="var(--orange)"/></svg>
        (555) 010-4821
      </li>
      <li>
        <svg viewBox="0 0 12 12"><rect x="1" y="2.5" width="10" height="7" fill="none" stroke="var(--orange)" stroke-width="1.2"/><path d="M1 2.5 L6 6.5 L11 2.5" fill="none" stroke="var(--orange)" stroke-width="1.2"/></svg>
        info@rmcoffeehouse.com
      </li>
      <li>
        <svg viewBox="0 0 12 12"><circle cx="6" cy="6" r="5" fill="none" stroke="var(--orange)" stroke-width="1.2"/><path d="M1 6 H11 M6 1 Q3 6 6 11 M6 1 Q9 6 6 11" fill="none" stroke="var(--orange)" stroke-width="1"/></svg>
        www.rmcoffeehouse.com
      </li>
    </ul>
    <p class="address">214b Harbour Lane, Lyttelton, NZ, 8082</p>
    <div class="socials">
      <span><i class="social-square"></i>rmcoffeehouse.com</span>
      <span><i class="social-circle"></i>rmcoffeehouse.com</span>
    </div>
    <div class="band band-grey"></div>
    <div class="band band-orange"></div>
  </section>
</body>
</html>
```